Brochure/flyer for our trip to Paris

Our company is taking us all on a summer trip to Paris. We have some key information that we need to tell everybody about the trip. We think a nicely designed brochure or flyer, which uses our brand colours and guidelines, would be something nice to keep during the trip and as a memento afterwards.

We are looking for a brochure or a flyer which contains all the info in the attached document.

This needs to happen really fast as we actually go to Paris on the 13th August. We also need time to print it!

We can provide a library of icons. All images in the document can be changed. you don't have to use the images in the document.

Target Market(s)

People in our company. They are fun and as this is for a party the flyer needs to feel uplifting.

Industry/Entity Type

Health

Font styles to use
Other font styles liked:
• Nexa - please see attached font.

Requirements
Must have
• Designers must stick to our brand guideline, font and the colours we use.
• Please also see attached content for the flyer.
• This website shows our style - https://www.kelotrix.com/fr
Should not have
• Please don't make it too tacky or too much about French things. It can be a bit playful but not too much.

```html
<!DOCTYPE html>
<html lang="en">
<head>
<meta charset="utf-8">
<title>Paris Trip Flyer</title>
<link href="https://fonts.googleapis.com/css2?family=Montserrat:wght@300;400;600;700&display=swap" rel="stylesheet">
<style>
:root{
  --navy:#0d4f8b;
  --sky:#3aaee2;
  --grey:#bfc1c3;
  --grey-light:#dedfe0;
  --ink:#3a3a3c;
  --paper:#ffffff;
  --backdrop:#ececed;
}
*{box-sizing:border-box;margin:0;padding:0}
html,body{width:1200px;height:960px;overflow:hidden}
body{background:var(--backdrop);font-family:"Montserrat",sans-serif;color:var(--ink)}
.flyer{position:absolute;left:280px;top:28px;width:640px;height:904px;background:var(--paper);overflow:hidden;box-shadow:0 2px 10px rgba(0,0,0,.12)}
.block{position:absolute}
h2{font-weight:600;font-size:21px;letter-spacing:.2px;line-height:1.2}
h3{font-weight:600;font-size:14px;margin-top:12px;line-height:1.3}
p,li{font-weight:300;font-size:10px;line-height:1.45}
.travel{left:0;top:0;width:370px;height:282px;background:var(--navy);color:#fff;padding:28px 24px 0 30px}
.travel h2{color:#fff}
.point{display:flex;gap:8px;align-items:flex-start;margin-top:6px}
.point svg{flex:0 0 13px;margin-top:1px}
.point p{color:#e8f0f8}
.tips{left:0;top:282px;width:370px;height:80px;background:var(--grey-light);padding:14px 24px 0 30px}
.tips h3{margin-top:0;color:var(--navy);font-size:15px}
.tips .point p{color:var(--ink);overflow-wrap:anywhere}
.phrases-a{left:0;top:362px;width:370px;height:128px;padding:16px 24px 0 30px}
.phrases-a h3{color:var(--navy);font-size:16px;margin:0 0 6px;line-height:1.2}
ol{list-style-position:inside}
.hotel-band{left:0;top:490px;width:370px;height:56px;background:var(--sky);color:#fff;display:flex;align-items:center;gap:12px;padding:0 30px}
.hotel-band p{color:#fff;font-size:10px;line-height:1.35}
.hotel-band strong{font-weight:600}
.phrases-b{left:0;top:546px;width:370px;height:220px;padding:14px 24px 0 30px}
.phrases-b li{line-height:1.4}
.metro{left:370px;top:0;width:270px;height:222px;padding:28px 24px 0 22px}
.metro h2,.hotel-info h2{color:var(--navy);font-size:15px}
.metro p{font-size:9.5px;margin-top:8px;text-align:justify}
.hotel-info{left:370px;top:222px;width:270px;height:268px;padding:6px 24px 0 22px}
.hotel-info .note{font-size:8.5px;margin:3px 0 8px}
.map{width:224px;height:196px;border:2px solid var(--sky);background:linear-gradient(135deg,#e9eaec,#d7d9dc)}
.phone-band{left:370px;top:490px;width:270px;height:56px;background:var(--navy);color:#fff;display:flex;align-items:center;gap:10px;padding:0 22px}
.phone-band p{color:#fff;font-weight:600;font-size:11.5px}
.emergency{left:370px;top:546px;width:270px;height:130px;background:var(--grey);color:#fff;padding:20px 22px 0 22px;display:flex;gap:12px}
.emergency h3{margin:0 0 6px;color:#fff;font-size:15px;line-height:1.2}
.emergency p{color:#f4f4f4;font-size:9.5px;line-height:1.5}
.brand{left:370px;top:676px;width:270px;height:90px;display:flex;flex-direction:column;align-items:center;justify-content:center}
.brand-name{font-weight:600;font-size:42px;color:var(--sky);letter-spacing:1px;line-height:1}
.brand-url{font-weight:400;font-size:10.5px;letter-spacing:3px;color:var(--ink);margin-top:8px}
.itinerary{left:0;top:766px;width:640px;height:138px;background:var(--sky);color:#fff;padding:14px 30px 0 30px}
.itinerary h2{color:#fff;font-size:17px;display:inline}
.itinerary .date{font-size:10px;font-weight:400;margin-left:6px}
.itinerary ul{margin-top:6px;padding-left:16px}
.itinerary li{color:#fff;font-size:10px;line-height:1.45}
</style>
</head>
<body>
<main class="flyer">

  <section class="block travel">
    <h2>Travel Information</h2>
    <h3>Outward Journey 13/08/16:</h3>
    <div class="point"><svg viewBox="0 0 14 14" width="13" height="13"><circle cx="7" cy="7" r="7" fill="#fff"/><path d="M4 7h5M7 4.5L9.5 7 7 9.5" stroke="#0d4f8b" stroke-width="1.6" fill="none"/></svg><p>Meet at Kings Cross St Pancras International Station no later than 6:55am.</p></div>
    <div class="point"><svg viewBox="0 0 14 14" width="13" height="13"><circle cx="7" cy="7" r="7" fill="#fff"/><path d="M4 7h5M7 4.5L9.5 7 7 9.5" stroke="#0d4f8b" stroke-width="1.6" fill="none"/></svg><p>Our train departs at 7:55am and arrives in Paris at 11:17am local time.</p></div>
    <h3>Return Journey 14/08/16:</h3>
    <div class="point"><svg viewBox="0 0 14 14" width="13" height="13"><circle cx="7" cy="7" r="7" fill="#fff"/><path d="M4 7h5M7 4.5L9.5 7 7 9.5" stroke="#0d4f8b" stroke-width="1.6" fill="none"/></svg><p>Meet at Gare Du Nord no later than 2pm.</p></div>
    <div class="point"><svg viewBox="0 0 14 14" width="13" height="13"><circle cx="7" cy="7" r="7" fill="#fff"/><path d="M4 7h5M7 4.5L9.5 7 7 9.5" stroke="#0d4f8b" stroke-width="1.6" fill="none"/></svg><p>Our train departs at 3:13pm and arrives in London at 4:30pm local time, please be on time.</p></div>
  </section>

  <section class="block tips">
    <h3>Top Tips</h3>
    <div class="point"><svg viewBox="0 0 14 14" width="13" height="13"><circle cx="7" cy="7" r="7" fill="#0d4f8b"/><path d="M4 7h5M7 4.5L9.5 7 7 9.5" stroke="#fff" stroke-width="1.6" fill="none"/></svg><p>The best way to find your way around is to use RouteNest or alternatively http://www.metroplan-paris.fr/itineraires/recherche</p></div>
  </section>

  <section class="block phrases-a">
    <h3>Some Must-know French Phrases for Savvy Travellers:</h3>
    <ol>
      <li>Bonjour (Hello)</li>
      <li>Oui / Non (Yes / No)</li>
      <li>Parlez-vous anglais ? (Do you speak English?)</li>
      <li>Où est le métro? (Where is the Metro?)</li>
    </ol>
  </section>

  <section class="block hotel-band">
    <svg viewBox="0 0 30 30" width="30" height="30"><circle cx="15" cy="15" r="15" fill="#fff"/><rect x="8" y="10" width="14" height="10" rx="1" fill="none" stroke="#3aaee2" stroke-width="1.6"/><path d="M8 10l7 6 7-6" fill="none" stroke="#3aaee2" stroke-width="1.6"/></svg>
    <p><strong>HÔTEL DES ORMES CLAIRS,</strong> 14 rue Valmonde<br>75001 Paris, France</p>
  </section>

  <section class="block phrases-b">
    <ol start="5">
      <li>Où est...? (Where is...?)</li>
      <li>Où est le guichet ? (Where is the ticket window?)</li>
      <li>Combien ça coûte? (How much does it cost?)</li>
      <li>Merci (Thank you!)</li>
      <li>Bonsoir (Hello/good evening)</li>
      <li>Au Revoir (Goodbye)</li>
      <li>Puis-je me connecter à Internet? (Can I get on the internet?)</li>
      <li>Je ne comprends pas. (I don't understand)</li>
      <li>Je ne sais pas. (I don't know)</li>
      <li>Est-ce que vous pouvez l'écrire? (Could you please write it down?)</li>
      <li>Pouvez-vous m'aider, s'il vous plaît? (Can you help me please?)</li>
    </ol>
  </section>

  <section class="block metro">
    <h2>How to use the metro:</h2>
    <p>You have each been given 3 Metro tickets to help you on your way, although you may need additional tickets depending on what your plans are in your free time. They are €4 for a single journey. Once you're in the Metro station, how to use the tickets is pretty self-explanatory. Tip from Delphine: the tickets have a magnetic strip, so try and keep them away from bank cards etc. If you find that any of your tickets do not work, you can ask at the kiosk for a replacement.</p>
  </section>

  <section class="block hotel-info">
    <h2>Hotel Information</h2>
    <p class="note">Nearest Metro Station: Chatelet (as pictured)</p>
    <div class="map" role="img" aria-label="Street map of the area around the hotel with a pin marking its location"></div>
  </section>

  <section class="block phone-band">
    <svg viewBox="0 0 30 30" width="30" height="30"><circle cx="15" cy="15" r="14" fill="none" stroke="#fff" stroke-width="1.6"/><path d="M11 8.5l2.5 3-1.5 1.8c.8 1.8 2 3 3.7 3.8l1.8-1.5 3 2.5-1.6 2.2c-4.8-.6-8.9-4.7-9.5-9.5z" fill="#fff"/></svg>
    <p>Tel: +33 1 40 00 17 58</p>
  </section>

  <section class="block emergency">
    <svg viewBox="0 0 30 30" width="30" height="30" style="flex:0 0 30px"><circle cx="15" cy="15" r="14" fill="none" stroke="#fff" stroke-width="1.6"/><path d="M11 8.5l2.5 3-1.5 1.8c.8 1.8 2 3 3.7 3.8l1.8-1.5 3 2.5-1.6 2.2c-4.8-.6-8.9-4.7-9.5-9.5z" fill="#fff"/></svg>
    <div>
      <h3>Emergency Internal Contacts:</h3>
      <p>Maren - 07700 900141<br>Tobias - 07700 900262<br>Idris - 07700 900383<br>Noor - 07700 900494</p>
    </div>
  </section>

  <section class="block brand">
    <span class="brand-name">Kelotrix</span>
    <span class="brand-url">www.kelotrix.com</span>
  </section>

  <section class="block itinerary">
    <h2>Itinerary</h2><span class="date">- 13th August</span>
    <ul>
      <li>Arrive in Paris at 11:17am local time</li>
      <li>Drop bags to hotel, grab lunch and enjoy our 1 hour River Seine Tour</li>
      <li>Free time 2:30pm (you will need to go and officially check in at the hotel and get ready for the evening within this time)</li>
      <li>7pm: Drinks and dinner at.....</li>
      <li>Late night drinks at.....</li>
    </ul>
  </section>

</main>
</body>
</html>
```